Quillora homepage (design only)

We need a high-impact design (alone) for the homepage for a new service to be launched shortly.

Quillora.com will allow consumers to generate a free 'financial personality' report which will help people protect themselves from being mis-sold inappropriate products and services by the financial services industry.

We have upload the Quillora logo and associated artwork. You have totally free reign to use these as you see fit, including using different colours to the lime green we've used.

We ONLY want a design and would prefer it in Illustrator CS5 or lower format rather than Photoshop bitmap. We will write any necessary code or CSS for the final page.

We intend the end site to utilise html5 type animation and effects extensively so if you are picturing an animation, please ensure you explain it with your submission.

The homepage will have five main elements:

1. Navigation:
- Why Quillora
- Security
- Sample report
- Do the test

2. Main section - Quillora : Know Your Financial Personality (you can add ipsum lorum 'explanatory text' if you see fit). This section should refer to the services output, a report which shows five financial characteristics:
- Personality type
- Investment approach
- Knowledge
- Decision biases
- % of UK population like you

3. 'See how you compare against the UK'. An important output of the report is the fact it is linked to extensive UK research. When a user has completed the test, Quillora show him or her via an info graphic, whist percentage of the UK population shares their attributes. Accompnaying tex reads: " If you've ever wondered how you compare to others when it comes to your attitudes on money related matters, quillora will show you". There is an attached file called 'infographic' that illustrates what the end infogrpahic might look like. You can choose to refer to this or elements of this in this section if you choose.

4. 'Cut out the stuff not relevant to you' Accompanying text could be: "Whether it’s language, unnecessarily complex products or stuff that may be too plain risky for you, your Quillora report will help filter out all of the stuff that’s less relevant to you leaving you with choices you understand and decisions that are easier to make." we imagine this section leading to a page that will explain the complexity of products and services before a Quillora report and the small number of relevant services after a quillora report. This section should illustrate that before and after concept.

5. 'Take the test' This section is critical, its the 'call to action' element of the page that links straight to the test. It should illustrate that the test is very short, and very easy.. only two very interactive steps before you get results:
1. Click on the graphics that best describe you.
2. Drag some questions into Quillora 'answer buckets'
3. Done! See the results.
4. Give your free profile to any online service (we make it simple)

The emphasis here is on illustration, typography, colour and impact. We want the site to feel consumer and accessible, not too stuffy and financial, at the same time not too childlike. We are not in favour of typical 'financial' library pics, we'd prefer illustration. Please use your own creativity

Target Market(s)

Adults typically aged 30+ with majority in 40's - 60's. People considering investing or taking any kind of financial advice,

Industry/Entity Type

Financial

Font styles to use
Sans Serif

Requirements
Must have
• The design must include the attached quillora logo albeit the colours used can be entirely at your discretion.
Nice to have
• Site designs we like include:
http://www.ferndashy.com

Should not have
• Design should not contain 'bamboo' clip art. If any quillora type artwork is needed, if should be a derivative of the attached 'bamboo stalk' file. Ideally no stock photography. Illustration and typography should dominate.

Should not use serif fonts

```html
<!DOCTYPE html>
<html lang="en">
<head>
<meta charset="utf-8">
<title>Quillora : Know Your Financial Personality</title>
<link rel="stylesheet" href="https://fonts.googleapis.com/css2?family=Arimo:wght@400;700&display=swap">
<style>
  :root {
    --lime: #8bc34a;
    --lime-bright: #7dc242;
    --lime-pale: #d6ecc0;
    --lime-mist: #eef7e6;
    --forest: #3f6b1f;
    --forest-text: #4a7a24;
    --footer: #5e9236;
    --footer-line: #86b35f;
    --ink: #222;
    --grey-line: #d8d8d8;
    --track: #6a6a6a;
    --bubble: #c4c4c4;
    --accent: #f47a3a;
    --white: #fff;
  }
  * { box-sizing: border-box; margin: 0; padding: 0; }
  html, body { width: 1200px; height: 2372px; overflow: hidden; }
  body { position: relative; background: var(--white); font-family: "Arimo", Arial, sans-serif; color: var(--ink); }
  .abs { position: absolute; }

  /* header + hero */
  .hero-art {
    left: 0; top: 0; width: 1200px; height: 540px;
    background: linear-gradient(180deg, var(--lime) 0%, #a9d47e 30%, var(--lime-pale) 70%, var(--lime-mist) 100%);
  }
  .top-bar { left: 0; top: 0; width: 1200px; height: 92px; background: linear-gradient(180deg, #9ccd68, #c5e4a4); border-bottom: 2px solid #b3d98c; }
  .brand { left: 172px; top: 12px; display: flex; align-items: center; gap: 14px; }
  .brand-dot { width: 70px; height: 70px; border-radius: 50%; background: var(--lime-bright); border: 3px solid var(--white); }
  .brand-name { font-size: 30px; color: var(--forest); font-weight: 400; }
  .main-nav { left: 475px; top: 56px; display: flex; font-size: 16px; color: var(--ink); }
  .main-nav span { display: block; }
  .nav-why { width: 190px; } .nav-security { width: 120px; } .nav-sample { width: 145px; }

  .hero-title { left: 186px; top: 186px; font-size: 72px; color: var(--white); font-weight: 400; }
  .hero-sub { left: 192px; top: 266px; font-size: 22px; color: var(--forest); }
  .features { left: 310px; top: 314px; list-style: none; }
  .features li { display: flex; align-items: center; height: 36px; font-size: 17px; color: var(--ink); }
  .features li::before { content: ""; width: 11px; height: 26px; background: var(--lime-bright); margin-right: 14px; }

  /* compare */
  .compare-title { left: 302px; top: 580px; font-size: 28px; color: var(--forest); }
  .compare-quote { left: 408px; top: 630px; width: 560px; font-size: 15px; line-height: 22px; color: var(--forest-text); }
  .rule { left: 0; width: 1200px; height: 3px; background: var(--grey-line); }
  .infographic { left: 0; top: 716px; }

  /* filter section */
  .filter-band { left: 0; top: 1160px; width: 1200px; height: 432px; background: var(--lime); }
  .filter-band::before { content: ""; position: absolute; left: 0; top: 0; width: 100%; height: 24px; background: #b2d88a; }
  .filter-title { left: 178px; top: 1310px; font-size: 33px; color: var(--white); }
  .filter-quote { left: 178px; top: 1374px; width: 860px; font-size: 17px; line-height: 24px; color: var(--white); }

  /* cta */
  .cta-button { left: 492px; top: 1694px; width: 222px; height: 54px; background: var(--lime); color: var(--white); font-size: 24px; font-weight: 700; display: flex; align-items: center; justify-content: center; box-shadow: 0 2px 4px rgba(0,0,0,.2); }
  .cta-steps { left: 380px; top: 1776px; font-size: 14px; line-height: 19px; color: var(--ink); list-style: none; }

  /* footer */
  .site-footer { left: 0; top: 1944px; width: 1200px; height: 428px; background: var(--footer); color: var(--white); }
  .site-footer .abs { color: var(--white); }
  .foot-brand { left: 162px; top: 104px; font-size: 32px; }
  .foot-dot { left: 215px; top: 152px; width: 76px; height: 76px; border-radius: 50%; background: var(--lime-bright); border: 3px solid var(--white); }
  .foot-col { border-left: 1px solid var(--footer-line); padding-left: 12px; font-size: 14px; line-height: 33px; }
  .foot-nav { left: 378px; top: 82px; }
  .foot-support-label { left: 470px; top: 240px; font-size: 20px; font-weight: 700; }
  .foot-support { left: 568px; top: 110px; line-height: 30px; }
  .keep-label { left: 742px; top: 94px; font-size: 14px; font-weight: 700; }
  .social { left: 864px; top: 78px; border-left: 1px solid var(--footer-line); padding-left: 10px; display: grid; gap: 6px; }
  .social span { display: block; width: 32px; height: 32px; background: #111; }
  .legal { top: 2342px; font-size: 11px; color: var(--white); }
  .legal-copy { font-weight: 700; }
</style>
</head>
<body>

  <div class="abs hero-art" role="img" aria-label="Bright green stalk-and-leaf illustration across the hero"></div>

  <header class="abs top-bar">
    <div class="abs brand"><span class="brand-dot"></span><span class="brand-name">Quillora</span></div>
    <nav class="abs main-nav">
      <span class="nav-why">Why&nbsp; Quillora</span>
      <span class="nav-security">Security</span>
      <span class="nav-sample">Sample report</span>
      <span>Do the test</span>
    </nav>
  </header>

  <h1 class="abs hero-title">Quillora</h1>
  <p class="abs hero-sub">Know Your Financial Personality</p>
  <ul class="abs features">
    <li>Personality type</li>
    <li>Investment approach</li>
    <li>Knowledge</li>
    <li>Decision biases</li>
    <li>% of UK population like you</li>
  </ul>

  <h2 class="abs compare-title">See how you compare against the UK</h2>
  <p class="abs compare-quote">"If you've ever wondered how you compare to others when it comes to your attitudes on money related matters, quillora will show you"</p>
  <div class="abs rule" style="top:708px"></div>

  <svg class="abs infographic" width="1200" height="444" viewBox="0 716 1200 444" font-family="Arimo, Arial, sans-serif">
    <path d="M244 792 V928 H508 V1090 H965 V1012" fill="none" stroke="var(--track)" stroke-width="6"/>
    <circle cx="244" cy="768" r="24" fill="#fff" stroke="var(--track)" stroke-width="6"/>
    <circle cx="965" cy="986" r="24" fill="#fff" stroke="var(--track)" stroke-width="6"/>
    <text x="280" y="766" font-size="12" fill="#555">Alex</text>
    <circle cx="286" cy="928" r="4" fill="var(--accent)"/>
    <circle cx="354" cy="928" r="4" fill="var(--accent)"/>
    <circle cx="580" cy="1090" r="4" fill="var(--accent)"/>
    <circle cx="762" cy="1090" r="4" fill="var(--accent)"/>
    <text x="265" y="958" font-size="13" fill="#555">Gender</text>
    <text x="342" y="958" font-size="13" fill="#555">Age</text>
    <text x="532" y="1110" font-size="13" fill="#555">Financial Knowledge</text>
    <text x="718" y="1110" font-size="13" fill="#555">Risk aptitude</text>
    <text x="922" y="877" font-size="12" fill="#555">% like me</text>
    <circle cx="284" cy="858" r="12" fill="var(--accent)"/>
    <text x="284" y="862" font-size="9" fill="#fff" text-anchor="middle">47%</text>
    <rect x="276" y="876" width="10" height="24" fill="#3aa6e8" role="img" aria-label="Male figure"/>
    <rect x="302" y="876" width="10" height="24" fill="#e08ce8" role="img" aria-label="Female figure"/>
    <g font-size="9" fill="#555">
      <rect x="342" y="820" width="14" height="10" fill="#aaa"/><text x="362" y="829">30's - 16%</text>
      <rect x="342" y="844" width="14" height="10" fill="#222"/><text x="362" y="853" fill="#222" font-weight="700">40's</text>
      <circle cx="402" cy="850" r="11" fill="var(--accent)"/><text x="402" y="853" font-size="9" fill="#fff" text-anchor="middle">12%</text>
      <rect x="342" y="868" width="14" height="10" fill="#aaa"/><text x="362" y="877">50's - 28%</text>
      <rect x="342" y="892" width="14" height="10" fill="#aaa"/><text x="362" y="901">60's - 15%</text>
    </g>
    <g font-size="11" fill="#fff" text-anchor="middle" font-weight="700">
      <circle cx="580" cy="852" r="18" fill="var(--bubble)"/><text x="580" y="856">17%</text>
      <circle cx="580" cy="912" r="24" fill="var(--accent)"/><text x="580" y="916">28%</text>
      <circle cx="580" cy="974" r="22" fill="var(--bubble)"/><text x="580" y="978">27%</text>
      <circle cx="580" cy="1036" r="22" fill="var(--bubble)"/><text x="580" y="1040">28%</text>
      <circle cx="762" cy="806" r="18" fill="#ddd"/><text x="762" y="810">10%</text>
      <circle cx="762" cy="858" r="18" fill="#fff" stroke="#eee"/><text x="762" y="862" fill="var(--accent)">16%</text>
      <circle cx="762" cy="920" r="24" fill="var(--bubble)"/><text x="762" y="924">23%</text>
      <circle cx="762" cy="984" r="24" fill="var(--bubble)"/><text x="762" y="988">25%</text>
      <circle cx="762" cy="1046" r="18" fill="#ddd"/><text x="762" y="1050">10%</text>
    </g>
    <rect x="938" y="886" width="52" height="14" fill="#3aa6e8" role="img" aria-label="Row of highlighted people figures"/>
    <rect x="938" y="904" width="52" height="40" fill="#c8c8c8" role="img" aria-label="Rows of grey people figures"/>
  </svg>

  <section class="abs filter-band"></section>
  <h2 class="abs filter-title">Cut out the stuff not relevant to you</h2>
  <p class="abs filter-quote">"Whether it's language, unnecessarily complex products or stuff that may be too plain risky for you, your Quillora report will help filter out all of the stuff that's less relevant to you leaving you with choices you understand and decisions that are easier to make."</p>

  <div class="abs rule" style="top:1648px"></div>
  <div class="abs cta-button">TAKE THE TEST</div>
  <ol class="abs cta-steps">
    <li>1. Click on the graphics that best describe you.</li>
    <li>2. Drag some questions into Quillora 'answer buckets'</li>
    <li>3. Done! See the results.</li>
    <li>4. Give your free profile to any online service (we make it simple)</li>
  </ol>
  <div class="abs rule" style="top:1926px"></div>

  <footer class="abs site-footer">
    <div class="abs foot-brand">Quillora</div>
    <div class="abs foot-dot"></div>
    <nav class="abs foot-col foot-nav">
      <div>Why&nbsp; Quillora</div><div>Security</div><div>Sample report</div><div>Do the test</div>
    </nav>
    <div class="abs foot-support-label">Support</div>
    <div class="abs foot-col foot-support">
      <div>home</div><div>FAQs</div><div>Sitemap</div><div>hello@quillora.com</div><div>004000400</div><div>Office</div><div>020 0007416</div>
    </div>
    <div class="abs keep-label">Keep in touch</div>
    <div class="abs social" aria-label="Social links"><span></span><span></span><span></span><span></span></div>
  </footer>
  <div class="abs legal" style="left:228px">Privacy policy</div>
  <div class="abs legal" style="left:342px">Site terms</div>
  <div class="abs legal" style="left:458px">Terms and conditions</div>
  <div class="abs legal" style="left:622px">Regulatory</div>
  <div class="abs legal legal-copy" style="left:744px">© 2014 Quillora Limited</div>

</body>
</html>
```